Tolvik's Trim spring flyers

I am needing a flyer design for my lawn mowing business. my services are mowing, edging, weed eating, vacuuming with strong attention to detail. residential and commercial. Mowing average $35 and Spring clean up average $79. Looking for fun, professional and colorful to grab the eye and stand out. rough sizing of 10"x4"

Target Market(s)

people needing lawn care and spring clean up

Font styles to use
Serif

Colors

Designer to choose colors to be used in the design.

Requirements
Must have
• Services listed and pricing listed
• please add licensed and insured
• 417-555-0183
• dorsebrian7@fernmail.test
• FREE ESTIMATES

```html
<!DOCTYPE html>
<html lang="en">
<head>
<meta charset="utf-8">
<title>Tolvik's Trim Lawn Care Flyer</title>
<link rel="stylesheet" href="https://fonts.googleapis.com/css2?family=Libre+Baskerville:wght@400;700&family=Bebas+Neue&display=swap">
<style>
  :root {
    --brand-blue: #1273bd;
    --charcoal: #3d3d3d;
    --lawn-green: #77b843;
    --grass-dark: #3f8a26;
    --grass-light: #8fcf4a;
    --white: #ffffff;
  }
  * { margin: 0; padding: 0; box-sizing: border-box; }
  html, body { width: 1200px; height: 3000px; overflow: hidden; background: var(--white); }
  .flyer {
    position: relative;
    width: 1200px;
    height: 3000px;
    overflow: hidden;
    background: var(--white);
    font-family: "Libre Baskerville", Georgia, serif;
    color: #1a1a1a;
  }
  .abs { position: absolute; }

  /* Brand block */
  .brand-mark { left: 540px; top: 88px; width: 120px; height: 120px; background: var(--brand-blue); }
  .brand-name {
    left: 0; top: 300px; width: 1200px; text-align: center;
    color: var(--brand-blue); font-weight: 700; text-transform: uppercase; line-height: 1;
  }
  .brand-name .line-main { display: block; font-size: 70px; letter-spacing: 1px; }
  .brand-name .line-sub { display: block; font-size: 30px; letter-spacing: 14px; margin-top: 22px; }

  .geometry { left: 0; top: 0; width: 1200px; height: 3000px; }

  /* Services */
  .services-bar { left: 117px; top: 1403px; width: 21px; height: 110px; background: var(--brand-blue); }
  .services-title { left: 160px; top: 1408px; font-size: 84px; font-weight: 400; color: var(--brand-blue); line-height: 1.1; }
  .services-list { left: 117px; top: 1525px; list-style: none; }
  .services-list li {
    position: relative; padding-left: 40px; font-size: 62px; line-height: 90px; color: #1a1a1a; white-space: nowrap;
  }
  .services-list li::before {
    content: ""; position: absolute; left: 0; top: 32px; width: 6px; height: 32px; background: var(--brand-blue);
  }

  .detail-frame { left: 582px; top: 1395px; width: 553px; height: 560px; border: 3px solid var(--brand-blue); }
  .detail-box {
    left: 618px; top: 1432px; width: 481px; height: 488px; background: var(--brand-blue);
    color: var(--white); font-weight: 700; font-size: 60px; line-height: 86px; text-align: center;
    display: flex; align-items: center; justify-content: center; text-transform: uppercase; white-space: nowrap;
  }

  /* Grass band */
  .grass-band {
    left: 0; top: 2014px; width: 1200px; height: 273px;
    background: linear-gradient(180deg, #4f8f2c 0%, #7fbf45 45%, #5d9b33 100%);
  }
  .market-frame {
    left: 140px; top: 2085px; width: 921px; height: 146px; border: 3px solid var(--white);
    color: var(--white); font-size: 54px; text-align: center; line-height: 140px; white-space: nowrap;
  }

  /* Pricing & contact */
  .price-zone {
    left: 0; top: 2325px; width: 1200px; height: 675px;
    background: linear-gradient(180deg, #5f9d34 0px, var(--lawn-green) 50px, var(--lawn-green) 100%);
  }
  .trust-line {
    left: 0; top: 2340px; width: 1200px; text-align: center; white-space: nowrap;
    color: var(--white); font-weight: 700; font-size: 36px; line-height: 50px; letter-spacing: 2px;
  }
  .price-label {
    left: 72px; width: 896px; height: 120px; background: var(--charcoal); color: var(--white);
    font-size: 58px; letter-spacing: 2px; text-align: center; line-height: 120px; white-space: nowrap;
  }
  .price-value {
    left: 990px; width: 138px; height: 120px; background: var(--brand-blue); color: var(--white);
    font-family: "Bebas Neue", "Arial Narrow", sans-serif; font-size: 104px; line-height: 132px; text-align: center;
  }
  .price-value sup { font-size: 36px; vertical-align: top; position: relative; top: -34px; margin-right: 2px; }
  .row-mowing { top: 2409px; }
  .row-spring { top: 2550px; }

  .phone-row {
    left: 0; top: 2712px; width: 1200px; height: 150px;
    display: flex; align-items: center; justify-content: center; gap: 28px;
  }
  .phone-icon { width: 140px; height: 140px; flex: none; }
  .phone-number {
    font-family: "Bebas Neue", "Arial Narrow", sans-serif;
    font-size: 150px; line-height: 1; color: var(--charcoal); letter-spacing: 3px; white-space: nowrap;
    padding-top: 12px;
  }
  .email {
    left: 0; top: 2876px; width: 1200px; text-align: center; font-size: 62px; color: var(--charcoal); white-space: nowrap;
  }
</style>
</head>
<body>
<div class="flyer">

  <svg class="abs geometry" viewBox="0 0 800 2000" width="1200" height="3000">
    <defs>
      <linearGradient id="lawnTone" x1="0" y1="0" x2="1" y2="1">
        <stop offset="0" stop-color="#8fcf4a"/>
        <stop offset="0.5" stop-color="#6cb53c"/>
        <stop offset="1" stop-color="#3f8a26"/>
      </linearGradient>
    </defs>
    <polygon points="0,355 290,425 0,510" fill="#1273bd"/>
    <polygon role="img" aria-label="Photo of a wide striped lawn with a person pushing a reel mower"
             points="0,510 800,275 800,715 520,795 0,940" fill="url(#lawnTone)"/>
    <polygon points="520,795 800,715 800,855" fill="#1273bd"/>
    <polygon points="0,680 800,870 800,905 0,715" fill="#3d3d3d"/>
  </svg>

  <div class="abs brand-mark"></div>
  <div class="abs brand-name">
    <span class="line-main">The Tolvik's Trim</span>
    <span class="line-sub">Lawn Care</span>
  </div>

  <div class="abs services-bar"></div>
  <h2 class="abs services-title">Services</h2>
  <ul class="abs services-list">
    <li>mowing</li>
    <li>edging</li>
    <li>weed eating</li>
    <li>vacuuming</li>
    <li>mowing</li>
  </ul>

  <div class="abs detail-frame"></div>
  <div class="abs detail-box"><p>With<br>strong<br>attention<br>to detail.</p></div>

  <div class="abs grass-band" role="img" aria-label="Close-up photo of fresh green grass blades"></div>
  <div class="abs market-frame">residential and commercial</div>

  <div class="abs price-zone" role="img" aria-label="Green grass tips fading into a solid green panel"></div>
  <div class="abs trust-line">FREE ESTIMATES &bull; LICENSED &amp; INSURED</div>

  <div class="abs price-label row-mowing">Mowing average</div>
  <div class="abs price-value row-mowing"><sup>$</sup>35</div>
  <div class="abs price-label row-spring">Spring clean up average</div>
  <div class="abs price-value row-spring"><sup>$</sup>79</div>

  <div class="abs phone-row">
    <svg class="phone-icon" viewBox="0 0 100 100" aria-label="Phone">
      <circle cx="50" cy="50" r="50" fill="#3d3d3d"/>
      <path fill="#ffffff" d="M33 22c3-2 6-1 8 2l6 10c1 3 0 5-2 7l-4 3c3 7 8 12 15 15l3-4c2-2 5-3 7-2l10 6c3 2 4 5 2 8l-4 6c-2 3-6 4-10 3-20-6-33-19-39-39-1-4 0-8 3-10z"/>
    </svg>
    <div class="phone-number">417 555 0183</div>
  </div>
  <div class="abs email">dorsebrian7@fernmail.test</div>

</div>
</body>
</html>
```